Letterhead & logo design project

We need a letterhead for a new company called Dornavelle Ltd a firm of Chartered Accountants and Chartered Tax Advisers based in Pangbourne, Berkshire
Updates
Please include the following:
Chartered Accountants and Chartered Tax Advisers
Industry/Entity Type
It Company
Requirements
Must have
- Must have director's name at the bottom of the letterhead. Must also contain some wording at the bottom of the page to be provided by the BQRPT at a later date

```html
<!DOCTYPE html>
<html lang="en">
<head>
<meta charset="utf-8">
<title>Dornavelle Ltd – Letterhead</title>
<link href="https://fonts.googleapis.com/css2?family=Crimson+Text:wght@400;600&display=swap" rel="stylesheet">
<style>
  :root {
    --paper: #ffffff;
    --ink: #1a1a1a;
    --brand: #9b4a57;
    --accent: #7d1526;
    --link: #8a1a2a;
  }
  * { margin: 0; padding: 0; box-sizing: border-box; }
  html, body {
    width: 848px;
    height: 1200px;
    overflow: hidden;
    background: var(--paper);
  }
  .letterhead {
    position: relative;
    width: 848px;
    height: 1200px;
    font-family: "Crimson Text", "Times New Roman", serif;
    color: var(--ink);
  }
  .brand-name {
    position: absolute;
    top: 22px;
    left: 0;
    width: 100%;
    text-align: center;
    font-size: 40px;
    font-weight: 600;
    letter-spacing: 1px;
    color: var(--brand);
    line-height: 1;
  }
  .brand-tagline {
    position: absolute;
    top: 72px;
    left: 0;
    width: 100%;
    text-align: center;
    font-size: 15px;
    letter-spacing: 2.5px;
    text-transform: uppercase;
    color: var(--brand);
    line-height: 1;
  }
  .contact {
    position: absolute;
    top: 111px;
    left: 0;
    width: 100%;
    text-align: center;
    font-size: 14px;
    line-height: 19px;
  }
  .contact .sep {
    color: var(--accent);
    font-weight: 600;
    margin: 0 5px;
  }
  .contact .web { color: var(--link); }
  .footer-rule {
    position: absolute;
    top: 1116px;
    left: 90px;
    width: 668px;
    height: 3px;
    background: var(--accent);
  }
  .footer-note {
    position: absolute;
    top: 1131px;
    left: 80px;
    width: 690px;
    font-size: 13.4px;
    white-space: nowrap;
    text-align: justify;
    text-align-last: justify;
  }
  .footer-note .sep { margin: 0 5px; }
</style>
</head>
<body>
  <div class="letterhead">
    <div class="brand-name">Dornavelle Ltd</div>
    <div class="brand-tagline">Chartered Accountants and Chartered Tax Advisers</div>

    <div class="contact">
      <p>Address 1, Address 2, Address 3, Address 4, Post Code<span class="sep">|</span>0118 4960213<span class="sep">|</span>07700 900418</p>
      <p>mtellwyn@dornavelleaccounts.com<span class="sep">|</span><span class="web">www.websiteaddress.com</span></p>
    </div>

    <div class="footer-rule"></div>
    <p class="footer-note">Director’s name<span class="sep">|</span>Must also contain some wording at the bottom of the page to be provided by the BQRPT at a later date</p>
  </div>
</body>
</html>
```